Snow & Ice Melter

We need a bag design for a new product our company is producing. Our company, Kestrel Winter Goods manufactures ice melt for melting snow. We are in the process of developing a new ice melt product called "Blizzard's Bane snow & ice melter". We would like to see designs that include a logo for the product, a snowman (that depicts Blizzard) and a wintery background. To get an idea of our current product packaging go to our website at http://www.kestrelwg.example

```html
<!DOCTYPE html>
<html lang="en">
<head>
<meta charset="utf-8">
<title>Blizzard's Bane snow &amp; ice melter</title>
<link rel="stylesheet" href="https://fonts.googleapis.com/css2?family=Open+Sans:wght@400;800&display=swap">
<style>
  :root {
    --ice-blue: #29a8e0;
    --tagline: #ffffff;
    --paper: #ffffff;
    --snow-edge: #3cbbea;
  }
  html, body {
    margin: 0;
    padding: 0;
    overflow: hidden;
    background: var(--paper);
  }
  .label {
    position: relative;
    width: 1200px;
    height: 534px;
    overflow: hidden;
    background: var(--paper);
  }
  .scenery {
    position: absolute;
    inset: 0;
    width: 1200px;
    height: 534px;
  }
  .product-name {
    position: absolute;
    left: 24px;
    top: 0;
    margin: 0;
    font-family: "Open Sans", Arial, sans-serif;
    font-weight: 800;
    font-size: 150px;
    line-height: 1.05;
    letter-spacing: -2px;
    color: var(--ice-blue);
    white-space: nowrap;
  }
  .product-name__line {
    display: block;
  }
  .product-name__line--second {
    margin-left: 470px;
  }
  .product-type {
    position: absolute;
    left: 580px;
    top: 320px;
    margin: 0;
    font-family: "Open Sans", Arial, sans-serif;
    font-weight: 400;
    font-size: 48px;
    line-height: 1;
    color: var(--tagline);
    white-space: nowrap;
  }
</style>
</head>
<body>
<main class="label">
  <svg class="scenery" viewBox="0 0 1200 534" xmlns="http://www.w3.org/2000/svg">
    <defs>
      <radialGradient id="night-glow" cx="0.5" cy="0.5" r="0.5">
        <stop offset="0" stop-color="#151515"/>
        <stop offset="0.35" stop-color="#2e2e2e"/>
        <stop offset="0.65" stop-color="#7a7a7a"/>
        <stop offset="0.88" stop-color="#d9d9d9"/>
        <stop offset="1" stop-color="#ffffff" stop-opacity="0"/>
      </radialGradient>
      <linearGradient id="snow-fill" x1="0" y1="380" x2="0" y2="534" gradientUnits="userSpaceOnUse">
        <stop offset="0" stop-color="#2fb4e8"/>
        <stop offset="0.35" stop-color="#bfe8f8"/>
        <stop offset="1" stop-color="#ffffff"/>
      </linearGradient>
      <linearGradient id="snowman-fill" x1="0" y1="0" x2="1" y2="1">
        <stop offset="0" stop-color="#ffffff"/>
        <stop offset="1" stop-color="#dcdfe3"/>
      </linearGradient>
    </defs>

    <ellipse class="night-sky" cx="830" cy="360" rx="700" ry="380" fill="url(#night-glow)"/>

    <path class="snow-drifts"
          d="M0 440 C80 425 150 460 260 445 C380 430 480 492 640 472 C800 455 900 392 1040 382 C1100 377 1150 400 1200 420 L1200 534 L0 534 Z"
          fill="url(#snow-fill)" stroke="var(--snow-edge)" stroke-width="3"/>

    <rect class="mascot-area" x="150" y="270" width="150" height="264" rx="75"
          fill="url(#snowman-fill)" role="img"
          aria-label="Illustration of Blizzard the snowman, three stacked snowballs with stick arms, standing in the snow"/>
  </svg>

  <h1 class="product-name">
    <span class="product-name__line">Blizzard’s</span>
    <span class="product-name__line product-name__line--second">Bane</span>
  </h1>
  <p class="product-type">snow and ice melter</p>
</main>
</body>
</html>
```